Crown and Dalmore
International Suspense. Corporate Intrigue. Greed. Passion. And Murder.
Project: Crown and Dalmore
Crown and Dalmore - Publishing
Creative Brief
Marissa Vaughn, a young woman and inexperienced corporate attorney, discovers that a series of murders is closely connected to an international conglomerate and masterfully concealed in its intricately linked layers of ownership, excess wealth and hidden agendas. For Marissa, the path to truth is confused by mystery, love, deception and danger and travels from New York City to Paris to New Orleans’ iconic French Quarter.

```html
<!DOCTYPE html>
<html lang="en">
<head>
<meta charset="utf-8">
<title>Crown &amp; Dalmore – Cover Spread</title>
<link rel="stylesheet" href="https://fonts.googleapis.com/css2?family=Oswald:wght@400;600;700&family=Roboto+Condensed:wght@400;700&display=swap">
<style>
  :root {
    --page-bg: #ffffff;
    --ink-dark: #1c1c1e;
    --ink-mid: #3a3a3d;
    --grey-light: #b9b9bb;
    --red-deep: #8e1014;
    --red-bright: #c8191e;
    --white: #ffffff;
  }
  * { margin: 0; padding: 0; box-sizing: border-box; }
  html, body { width: 1200px; height: 432px; overflow: hidden; background: var(--page-bg); }
  .canvas { position: relative; width: 1200px; height: 432px; }

  .spread {
    position: absolute; left: 210px; top: 0;
    width: 780px; height: 432px;
    display: flex;
    background: var(--ink-dark);
    color: var(--white);
    font-family: "Roboto Condensed", Arial, sans-serif;
  }
  .panel { position: relative; height: 100%; overflow: hidden; }
  .back-cover { width: 345px; }
  .spine { width: 50px; border-left: 1px solid rgba(255,255,255,.15); border-right: 1px solid rgba(255,255,255,.15); }
  .front-cover { width: 385px; }

  .cover-art { position: absolute; inset: 0; }
  .back-cover .cover-art {
    background:
      radial-gradient(ellipse 55% 35% at 30% 55%, var(--red-bright) 0%, var(--red-deep) 45%, transparent 75%),
      radial-gradient(ellipse 40% 30% at 70% 80%, var(--red-deep) 0%, transparent 70%),
      linear-gradient(180deg, var(--ink-mid) 0%, var(--ink-dark) 55%, #2a2a2c 100%);
  }
  .spine .cover-art {
    background:
      radial-gradient(ellipse 90% 25% at 50% 35%, var(--red-bright) 0%, transparent 80%),
      linear-gradient(180deg, var(--ink-mid), var(--ink-dark));
  }
  .front-cover .cover-art {
    background:
      radial-gradient(ellipse 45% 40% at 12% 60%, var(--red-bright) 0%, var(--red-deep) 50%, transparent 80%),
      radial-gradient(ellipse 30% 22% at 20% 92%, var(--red-deep) 0%, transparent 75%),
      linear-gradient(180deg, #2b2b2d 0%, #4a4a4d 45%, var(--grey-light) 68%, #6f6f72 82%, #2e2e30 100%);
  }

  .title {
    font-family: "Oswald", Impact, sans-serif;
    font-weight: 700; line-height: .9; text-transform: uppercase;
  }
  .tagline { font-size: 10.5px; line-height: 1.25; }

  .back-cover .title { position: absolute; left: 18px; top: 34px; font-size: 40px; }
  .back-cover .tagline { position: absolute; left: 18px; top: 114px; width: 140px; font-size: 8.5px; }
  .info-box { position: absolute; right: 40px; top: 40px; width: 70px; height: 78px; background: var(--white); }
  .blurb {
    position: absolute; left: 18px; top: 160px; width: 300px;
    font-size: 8.5px; line-height: 1.45; color: rgba(255,255,255,.9);
  }
  .blurb p + p { margin-top: 6px; }
  .back-cover .byline { position: absolute; right: 24px; bottom: 30px; text-align: left; }

  .byline {
    font-family: "Oswald", Arial, sans-serif; font-weight: 600;
    font-size: 13px; line-height: 1.25; text-transform: uppercase; letter-spacing: .03em;
  }

  .spine-text {
    position: absolute; left: 50%; top: 16px;
    writing-mode: vertical-rl;
    transform: translateX(-50%);
    display: flex; gap: 22px; align-items: center;
  }
  .spine .title { font-size: 26px; line-height: 1; }
  .spine .byline { font-size: 12px; line-height: 1.1; }

  .front-cover .title { position: absolute; left: 24px; top: 26px; font-size: 62px; }
  .front-cover .tagline { position: absolute; left: 26px; top: 146px; width: 190px; }
  .front-cover .byline { position: absolute; left: 26px; bottom: 30px; font-size: 15px; }
</style>
</head>
<body>
<main class="canvas">
  <section class="spread">
    <div class="panel back-cover">
      <div class="cover-art" role="img" aria-label="Dark monochrome city scene washed with red paint splatter"></div>
      <h2 class="title">Crown &amp;<br>Dalmore</h2>
      <p class="tagline">International Suspense. Corporate Intrigue. Greed. Passion. And Murder.</p>
      <div class="info-box"></div>
      <div class="blurb">
        <p>A young attorney uncovers a trail of murders hidden inside the layered ownership of a vast international conglomerate, where wealth and secrets shield the guilty.</p>
        <p>From New York to Paris to the French Quarter, every clue pulls her deeper into love, deception and danger she never expected to face.</p>
        <p>Each answer costs more than the last, and the truth may cost her everything.</p>
      </div>
      <p class="byline">By Ted Warbeck<br>&amp; Delia K. Morrow</p>
    </div>

    <div class="panel spine">
      <div class="cover-art" role="img" aria-label="Dark spine background with red splatter"></div>
      <div class="spine-text">
        <span class="title">Crown &amp; Dalmore</span>
        <span class="byline">By Ted Warbeck<br>&amp; Delia K. Morrow</span>
      </div>
    </div>

    <div class="panel front-cover">
      <div class="cover-art" role="img" aria-label="Black and white collage of the Eiffel Tower, a French Quarter cathedral and an arched bridge, splashed with red paint"></div>
      <h1 class="title">Crown &amp;<br>Dalmore</h1>
      <p class="tagline">International Suspense. Corporate Intrigue. Greed. Passion. And Murder.</p>
      <p class="byline">By Ted Warbeck<br>&amp; Delia K. Morrow</p>
    </div>
  </section>
</main>
</body>
</html>
```